Quill Ridge Business cards

We need business cards for our aviation company called Quill Ridge Aviation. The colour scheme is the same as the one in the logo you design (metallic green/ similar to the colours on the aircraft). The design needs to be unique and stand out.

Industry/Entity Type

Business

```html
<!DOCTYPE html>
<html lang="en">
<head>
<meta charset="utf-8">
<title>Quill Ridge Aviation – Business Cards</title>
<link rel="stylesheet" href="https://fonts.googleapis.com/css2?family=Arimo:wght@400;700&display=swap">
<style>
  :root {
    --page-bg: #ececec;
    --card-green: #5e7142;
    --brand-green: #5b7a3c;
    --ink: #2e2e2e;
    --band-dark: #3a3a3a;
    --white: #ffffff;
    --faint: rgba(255,255,255,0.16);
  }
  * { box-sizing: border-box; margin: 0; padding: 0; }
  html, body { width: 1043px; height: 1200px; overflow: hidden; }
  body {
    background: var(--page-bg);
    font-family: "Arimo", Arial, sans-serif;
    position: relative;
  }
  .card {
    position: absolute;
    left: 83px;
    width: 864px;
    height: 494px;
    overflow: hidden;
    box-shadow: 0 3px 10px rgba(0,0,0,0.28);
  }
  .card-front { top: 57px; background: var(--card-green); }
  .card-back { top: 586px; background: var(--white); }

  .front-ring {
    position: absolute;
    left: 322px; top: 86px;
    width: 400px; height: 400px;
    border: 38px solid var(--faint);
    border-radius: 50%;
  }
  .front-web {
    position: absolute;
    left: 16px; top: 452px;
    color: var(--white);
    font-size: 22px;
  }
  .front-brand {
    position: absolute;
    right: 24px; top: 300px;
    display: flex; flex-direction: column; align-items: center;
    color: var(--white);
  }
  .front-brand .dot {
    width: 96px; height: 96px;
    border: 12px solid var(--white);
    border-radius: 50%;
    margin-bottom: 14px;
  }
  .front-brand .name { font-size: 22px; font-weight: 700; letter-spacing: 0.3px; }

  .back-brand {
    position: absolute;
    left: 78px; top: 42px;
    display: flex; flex-direction: column; align-items: center;
    color: var(--brand-green);
  }
  .back-brand .dot {
    width: 82px; height: 82px;
    border: 11px solid var(--ink);
    border-radius: 50%;
    margin-bottom: 20px;
  }
  .back-brand .name { font-size: 22px; font-weight: 700; }

  .person {
    position: absolute;
    right: 59px; top: 190px;
    text-align: right;
  }
  .person .full-name { font-size: 34px; color: var(--ink); font-weight: 400; }
  .person .role { font-size: 16px; color: var(--brand-green); margin-top: 2px; }

  .divider {
    position: absolute;
    left: 0; top: 260px;
    width: 805px; height: 3px;
    background: var(--brand-green);
  }

  .contacts {
    position: absolute;
    left: 70px; top: 318px;
    list-style: none;
    font-size: 19px; color: var(--ink);
  }
  .contacts li { display: flex; align-items: center; height: 25.5px; }
  .contacts svg { width: 15px; height: 15px; margin-right: 11px; fill: var(--ink); }

  .address {
    position: absolute;
    left: 588px; top: 366px;
    display: flex; align-items: flex-start;
    font-size: 19px; color: var(--ink); line-height: 25px;
  }
  .address svg { width: 14px; height: 18px; margin: 3px 10px 0 0; fill: var(--ink); }

  .back-bands { position: absolute; left: 0; bottom: 0; }
</style>
</head>
<body>
  <section class="card card-front">
    <div class="front-ring"></div>
    <p class="front-web">www.quillridgeaviation.com</p>
    <div class="front-brand">
      <span class="dot"></span>
      <span class="name">QUILL RIDGE AVIATION</span>
    </div>
  </section>

  <section class="card card-back">
    <div class="back-brand">
      <span class="dot"></span>
      <span class="name">QUILL RIDGE AVIATION</span>
    </div>

    <div class="person">
      <p class="full-name">Daniel Okoro</p>
      <p class="role">GENERAL MANAGER</p>
    </div>

    <div class="divider"></div>

    <ul class="contacts">
      <li><svg viewBox="0 0 16 16"><path d="M4 0h8a1 1 0 0 1 1 1v14a1 1 0 0 1-1 1H4a1 1 0 0 1-1-1V1a1 1 0 0 1 1-1zm1 2v10h6V2zm3 11a1 1 0 1 0 0 2 1 1 0 0 0 0-2z"/></svg>+210400512630, +210400718245</li>
      <li><svg viewBox="0 0 16 16"><path d="M3.6 0.5l2.3 2.8-1.4 2a9 9 0 0 0 6.2 6.2l2-1.4 2.8 2.3-1.6 2.6C7 14.5 1.5 9 0.99 2.1z"/></svg>+210400936152, +250700314089</li>
      <li><svg viewBox="0 0 16 16"><path d="M0 3h16v10H0zm1.5 1.4v0.3L8 9l6.5-4.3v-0.3z"/></svg>gm@quillridgeaviation.com</li>
      <li><svg viewBox="0 0 16 16"><path d="M8 0a8 8 0 1 0 0 16A8 8 0 0 0 8 0zm0 2a6 6 0 0 1 5.6 4H2.4A6 6 0 0 1 8 2zM2.1 8h11.8a6 6 0 0 1-.3 2H2.4a6 6 0 0 1-.3-2z"/></svg>www.quillridgeaviation.com</li>
    </ul>

    <div class="address">
      <svg viewBox="0 0 14 18"><path d="M7 0a7 7 0 0 0-7 7c0 5 7 11 7 11s7-6 7-11a7 7 0 0 0-7-7zm0 4a3 3 0 1 1 0 6 3 3 0 0 1 0-6z"/></svg>
      <span>Kestrel Field Airport,<br>Northgate, Westmark</span>
    </div>

    <svg class="back-bands" width="864" height="62" viewBox="0 0 864 62">
      <polygon points="0,34 543,34 529,62 0,62" fill="var(--band-dark)"/>
      <polygon points="557,3 864,3 864,62 531,62" fill="var(--card-green)"/>
    </svg>
  </section>
</body>
</html>
```